Business Card Design Project

We are looking to redesign the logo, business card and stationary of one of our group companies - KESTRAL SUPPLY COMPANY LLC.

The company specialises in industrial PVC and CPVC Piping systems. It is situated in the Middle East and the focus is purely in this region.

The logo work is already completed. The file is uploaded for the reference.

We are looking for a clean minimalistic design for the business card.

regards
Ormund
Updates

Hello Everyone!

Thanks for submitting your designs. 

Yet to find the right design. Probably the below links will give you guys some more idea on what we would like.

Minimalist design with some creativity.

Ormund

http://plaincardgallery.example/inspiration/15-beautifully-minimal-business-cards

http://www.quietlayouthub.example/2011/11/14/30-minimalist-business-card-design/

http://www.firmpixelnotes.example/inspiration/minimal-business-cards/

Target Market(s)

Industrial users

Industry/Entity Type

Industrial

Requirements
Must have
• - Minimalistic design

- Back side of the card should include the manufacturer BRAVOLINE CANADA's decal. The file is upload for the reference

- Further information
Company Name:
KESTRAL SUPPLY COMPANY LLC
Address:
PO Box 9087, Sharjah Industrial Area 5, Qutrani Road
Sharjah, United Arab Emirates
Telephone:
+971-6-5018-392
Fax:
+977-6-5018-393
Email:
mail@ksc-holding.example

- FYI, Kestral Supply Company LLC is the authorised distributor for BRAVOLINE CANADA in the UAE. For further information on bravoline please visit the website www.bravoline.example

```html
<!DOCTYPE html>
<html lang="en">
<head>
<meta charset="utf-8">
<title>Kestral Supply Company LLC – Business Card</title>
<link rel="stylesheet" href="https://fonts.googleapis.com/css2?family=Didact+Gothic&family=Mulish:wght@800&display=swap">
<style>
  :root {
    --page: #e9e7e4;
    --card-dark: #2f2f2f;
    --card-dark-top: #262626;
    --text-light: #d6d6d6;
    --text-soft: #c4c4c4;
    --accent-blue: #86a9d6;
    --strip-blue: #7f9fc4;
    --badge-grey: #8c8c8c;
    --row-mid: #8f8f8f;
    --row-light: #d9d9d9;
    --row-text-on-mid: #f2f2f2;
    --row-text-on-light: #6e6e6e;
    --header-dark: #2c2c2c;
    --footer-white: #fbfbfb;
    --footer-text: #2a2a2a;
    --divider: #6a6a6a;
  }
  * { box-sizing: border-box; margin: 0; padding: 0; }
  html, body { width: 1200px; height: 1200px; overflow: hidden; }
  body {
    background: var(--page);
    font-family: "Didact Gothic", "Century Gothic", sans-serif;
    position: relative;
  }
  .card {
    position: absolute;
    left: 150px;
    width: 900px;
    height: 514px;
    overflow: hidden;
    box-shadow: 0 6px 18px rgba(0,0,0,0.18);
  }

  /* Front */
  .card-front {
    top: 60px;
    background: linear-gradient(160deg, var(--card-dark-top), var(--card-dark) 60%);
  }
  .front-details {
    position: absolute;
    right: 48px;
    top: 62px;
    text-align: right;
    color: var(--text-soft);
  }
  .company-name {
    font-family: "Mulish", "Century Gothic", sans-serif;
    font-weight: 800;
    font-size: 38px;
    letter-spacing: 1px;
    color: var(--text-light);
    margin-bottom: 26px;
  }
  .address { font-size: 24px; line-height: 32px; letter-spacing: 0.6px; }
  .contact { margin-top: 10px; font-size: 24px; line-height: 32px; letter-spacing: 0.6px; }
  .contact-line { display: flex; justify-content: flex-end; align-items: center; gap: 10px; }
  .contact-line svg { width: 18px; height: 18px; fill: var(--accent-blue); }
  .contact-line.email { margin-top: 16px; }
  .contact-line.web { color: var(--accent-blue); letter-spacing: 1.4px; }
  .side-strip {
    position: absolute; left: 0; top: 360px;
    width: 16px; height: 154px;
    background: var(--strip-blue);
  }
  .brand-mark {
    position: absolute; left: 110px; top: 404px;
    display: flex; align-items: center; gap: 14px;
  }
  .brand-square { width: 44px; height: 44px; background: var(--badge-grey); }
  .brand-name { font-size: 26px; color: var(--text-light); letter-spacing: 1px; }

  /* Back */
  .card-back { top: 626px; background: var(--footer-white); }
  .grid-header {
    position: absolute; left: 0; top: 0; width: 100%; height: 60px;
    background: var(--header-dark);
  }
  .grid-row { position: absolute; left: 0; width: 100%; height: 60px; }
  .grid-row.mid { background: var(--row-mid); color: var(--row-text-on-mid); }
  .grid-row.light { background: var(--row-light); color: var(--row-text-on-light); }
  .cell {
    position: absolute; top: 0; width: 50%; height: 60px;
    display: flex; align-items: center; justify-content: center;
    font-size: 34px; letter-spacing: 1.5px;
  }
  .cell.left { left: 0; }
  .cell.right { left: 50%; }
  .grid-header .cell { color: var(--text-light); font-size: 30px; }
  .column-divider {
    position: absolute; left: 450px; top: 60px;
    width: 2px; height: 300px; background: var(--divider);
  }
  .distributor-note {
    position: absolute; left: 30px; top: 378px;
    font-size: 20px; color: var(--footer-text);
  }
  .partner-mark {
    position: absolute; right: 32px; top: 440px;
    display: flex; align-items: center; gap: 10px;
  }
  .partner-square { width: 36px; height: 36px; background: var(--footer-text); }
  .partner-name { font-size: 30px; color: var(--footer-text); }
</style>
</head>
<body>

<section class="card card-front" aria-label="Card front">
  <div class="front-details">
    <h1 class="company-name">KESTRAL SUPPLY COMPANY LLC</h1>
    <p class="address">PO Box 9087, Sharjah Industrial<br>Area 5, Qutrani Road<br>Sharjah, United Arab Emirates</p>
    <div class="contact">
      <p class="contact-line">
        <svg viewBox="0 0 24 24" aria-hidden="true"><path d="M6.6 10.8a15 15 0 0 0 6.6 6.6l2.2-2.2c.3-.3.7-.4 1-.2 1.1.4 2.3.6 3.6.6.6 0 1 .4 1 1V20c0 .6-.4 1-1 1A17 17 0 0 1 3 4c0-.6.4-1 1-1h3.5c.6 0 1 .4 1 1 0 1.2.2 2.4.6 3.6.1.3 0 .7-.2 1z"/></svg>
        +971-6-5018-392
      </p>
      <p class="contact-line">
        <svg viewBox="0 0 24 24" aria-hidden="true"><path d="M7 3h10v5H7zM4 9h16a2 2 0 0 1 2 2v6h-4v4H6v-4H2v-6a2 2 0 0 1 2-2zm4 7v3h8v-3z"/></svg>
        +977-6-5018-393
      </p>
      <p class="contact-line email">
        <svg viewBox="0 0 24 24" aria-hidden="true"><path d="M2 5h20v14H2zm2 2v.5l8 5 8-5V7z"/></svg>
        mail@ksc-holding.example
      </p>
      <p class="contact-line web">
        <svg viewBox="0 0 24 24" aria-hidden="true"><path d="M12 2a10 10 0 1 0 0 20 10 10 0 0 0 0-20zm6.9 6h-3a15 15 0 0 0-1.3-3.9A8 8 0 0 1 18.9 8zM12 4c.9 1.2 1.6 2.5 2 4h-4c.4-1.5 1.1-2.8 2-4zM4.3 14a8 8 0 0 1 0-4h3.4a16 16 0 0 0 0 4zm.8 2h3a15 15 0 0 0 1.3 3.9A8 8 0 0 1 5.1 16zm3-8h-3a8 8 0 0 1 4.3-3.9C8.8 5.3 8.4 6.6 8.1 8zM12 20c-.9-1.2-1.6-2.5-2-4h4c-.4 1.5-1.1 2.8-2 4zm2.3-6H9.7a14 14 0 0 1 0-4h4.6a14 14 0 0 1 0 4zm.3 5.9c.6-1.2 1-2.5 1.3-3.9h3a8 8 0 0 1-4.3 3.9zM16.3 14a16 16 0 0 0 0-4h3.4a8 8 0 0 1 0 4z"/></svg>
        www.bravoline.example
      </p>
    </div>
  </div>
  <div class="side-strip"></div>
  <div class="brand-mark">
    <span class="brand-square"></span>
    <span class="brand-name">Kestral</span>
  </div>
</section>

<section class="card card-back" aria-label="Card back">
  <div class="grid-header">
    <span class="cell left">PRODUCTS</span>
    <span class="cell right">CAPABILITY</span>
  </div>
  <div class="grid-row light" style="top:60px"><span class="cell left">PIPES</span><span class="cell right" style="background:var(--row-mid);color:var(--row-text-on-mid)">DESIGN</span></div>
  <div class="grid-row mid" style="top:120px"><span class="cell left">FITTINGS</span><span class="cell right" style="background:var(--row-light);color:var(--row-text-on-light)">LOGISTICS</span></div>
  <div class="grid-row light" style="top:180px"><span class="cell left">VALVES</span><span class="cell right" style="background:var(--row-mid);color:var(--row-text-on-mid)">FINANCE</span></div>
  <div class="grid-row mid" style="top:240px"><span class="cell left" style="background:var(--row-light);color:var(--row-text-on-light)">ACCESSORIES</span><span class="cell right" style="background:var(--row-light);color:var(--row-text-on-light)">SOFTWARE</span></div>
  <div class="grid-row mid" style="top:300px"><span class="cell left">ENGINEERING</span><span class="cell right">INFRASTRUCTURE</span></div>
  <div class="column-divider"></div>
  <p class="distributor-note">Kestral Supply Company LLC, authorised distributor for</p>
  <div class="partner-mark">
    <span class="partner-square"></span>
    <span class="partner-name">Bravoline Canada</span>
  </div>
</section>

</body>
</html>
```